Need a flyer to leave behind when visiting clients or at shows

Glossy colorful tri-fold flyer with the same information that is on my web site www.brevalinkpro.com. I am open to a little modern or creative take on the typical brochure. I created the web site so I can provide any raw files needed from it. I would also like the ability to edit this flyer in the future in Adobe Photoshop Elements

```html
<!DOCTYPE html>
<html lang="en">
<head>
<meta charset="utf-8">
<title>BrevaLink Pro Tri-fold Brochure</title>
<link rel="stylesheet" href="https://fonts.googleapis.com/css2?family=Oswald:wght@300;400;500&family=Montserrat:wght@300;400;500;600;700&family=Open+Sans:wght@400;600&display=swap">
<style>
:root{
  --backdrop:#fbe90a;
  --purple:#4f2d8c;
  --purple-soft:#6b3fa6;
  --ink:#1d1d1d;
  --white:#ffffff;
  --dark:#1b1b1f;
  --panel:rgba(10,10,12,.82);
}
*{margin:0;padding:0;box-sizing:border-box}
html,body{width:1200px;height:1200px;overflow:hidden;background:var(--backdrop)}
body{position:relative;font-family:"Montserrat",sans-serif;color:var(--ink)}
.sheet{position:absolute;background:var(--white);overflow:hidden}
.sheet-outside{left:272px;top:54px;width:656px;height:510px}
.sheet-inside{left:257px;top:606px;width:686px;height:532px}
.abs{position:absolute}
.block-purple{position:absolute;background:var(--purple)}
.photo{position:absolute}

/* outside: core values */
.values-title{left:26px;top:292px;font-family:"Oswald",sans-serif;font-weight:500;font-size:22px;line-height:26px;color:var(--ink);letter-spacing:.3px;white-space:nowrap}
.value{position:absolute;left:28px;display:flex;align-items:center}
.value-icon{width:34px;height:34px;background:var(--purple);display:flex;align-items:center;justify-content:center;flex:none}
.value-label{margin-left:18px;font-size:10px;color:var(--purple);text-transform:uppercase;line-height:12px;font-weight:500}

/* outside: leadership */
.leader-title{left:239px;top:28px;font-family:"Oswald",sans-serif;font-weight:300;font-size:22px;color:var(--ink)}
.leader{left:237px;top:66px;width:180px;font-size:5.6px;line-height:10.2px;text-align:justify;color:var(--ink)}
.leader-card{float:left;width:84px;margin-right:5px;margin-bottom:2px}
.headshot{width:78px;height:96px;background:linear-gradient(160deg,#d9d9d9,#6f7378 60%,#2c2f33)}
.leader-name{font-size:11px;line-height:16px;color:var(--purple);margin-top:4px;text-align:left;white-space:nowrap}
.leader-role{font-size:7.6px;line-height:15px;color:var(--purple);text-align:left;letter-spacing:.2px;white-space:nowrap}
.contact{left:237px;top:277px;width:180px;height:68px;border:1.5px solid var(--purple);padding:9px 0 0 27px}
.contact-line{display:flex;align-items:center;font-size:9px;line-height:17.5px;color:var(--ink);white-space:nowrap}
.contact-line svg{margin-right:5px;flex:none}

/* outside: cover */
.cover-text{left:451px;color:var(--white);text-shadow:0 1px 2px rgba(0,0,0,.4);white-space:nowrap}
.cover-1{top:180px;font-size:24px;font-weight:300;letter-spacing:.5px}
.cover-2{top:212px;font-size:24px;font-weight:700}
.cover-3{top:243px;font-size:17px;font-weight:700}
.cover-4{top:268px;font-size:13px;font-weight:700}
.brand{left:447px;top:400px;font-family:"Montserrat",sans-serif;font-weight:700;font-size:15px;line-height:20px;color:var(--purple);display:flex;align-items:center;white-space:nowrap}
.brand-square{width:10px;height:10px;background:var(--purple);margin-right:7px}
.web{left:452px;top:467px;display:flex;align-items:center;font-size:9px;font-weight:600;color:var(--ink);white-space:nowrap}
.web svg{margin-right:9px}
.rule{left:600px;top:394px;width:1px;height:116px;background:#9a9a9a}
.rule-dot{left:597px;top:390px;width:7px;height:7px;border-radius:50%;background:var(--ink)}

/* inside: objectives */
.objectives-title{left:27px;top:268px;font-family:"Oswald",sans-serif;font-weight:400;font-size:30px;line-height:34px;color:var(--purple);text-transform:uppercase;letter-spacing:.5px}
.objective{position:absolute;left:18px;display:flex;align-items:center}
.objective-icon{width:34px;height:34px;border-radius:50%;background:var(--purple);display:flex;align-items:center;justify-content:center;flex:none}
.objective-text{margin-left:7px;font-size:10px;line-height:12px;color:var(--ink);width:160px}

/* inside: services */
.services{left:235px;top:20px;width:222px;height:506px;background:linear-gradient(180deg,#3b3d44,#25262b 45%,#2e2a26)}
.services-box{left:253px;top:142px;width:188px;height:316px;background:var(--panel)}
.services-our{left:278px;top:52px;font-size:36px;font-weight:300;color:var(--white);line-height:40px}
.services-title{left:278px;top:88px;font-size:29px;font-weight:700;color:var(--white);line-height:34px}
.services-copy{left:270px;top:153px;width:154px;font-size:7.6px;line-height:13.6px;text-align:justify;color:#e6e6e6;letter-spacing:.2px}
.services-head{left:270px;top:282px;font-size:12.5px;color:var(--white)}
.services-list{left:270px;top:304px;list-style:none}
.services-list li{display:flex;align-items:center;font-family:"Open Sans",sans-serif;font-size:7px;line-height:18px;color:#e6e6e6}
.services-list svg{margin-right:3px}

/* inside: about */
.about-title{left:474px;top:22px;font-family:"Oswald",sans-serif;font-weight:300;font-size:30px;color:var(--purple)}
.about-head{left:474px;font-size:13px;color:var(--ink)}
.about-copy{left:474px;width:200px;font-size:7.4px;line-height:16px;font-weight:600;color:var(--ink)}
</style>
</head>
<body>

<section class="sheet sheet-outside" aria-label="Brochure outside spread">
  <div class="block-purple" style="left:0;top:23px;width:230px;height:220px"></div>
  <div class="photo" role="img" aria-label="Close-up of a screen showing the word security with a hand cursor" style="left:0;top:51px;width:214px;height:235px;background:radial-gradient(circle at 55% 40%,#2a4a66,#101418 70%)"></div>

  <h2 class="abs values-title">OUR CORE VALUES</h2>
  <div class="value" style="top:328px">
    <div class="value-icon"><svg width="18" height="18" viewBox="0 0 18 18" fill="none" stroke="#fff" stroke-width="1.2"><circle cx="9" cy="9" r="7.5"/><circle cx="9" cy="7" r="2.2"/><path d="M5 13c1-2 2.5-3 4-3s3 1 4 3"/></svg></div>
    <span class="value-label">Client Focused</span>
  </div>
  <div class="value" style="top:372px">
    <div class="value-icon"><svg width="20" height="18" viewBox="0 0 20 18" fill="none" stroke="#fff" stroke-width="1.2"><circle cx="5" cy="4" r="2"/><circle cx="15" cy="4" r="2"/><path d="M2 17v-7h6v7M12 17v-7h6v7M7 11h6"/></svg></div>
    <span class="value-label">Accountability</span>
  </div>
  <div class="value" style="top:418px">
    <div class="value-icon"><svg width="18" height="18" viewBox="0 0 18 18" fill="#fff"><circle cx="8" cy="7" r="5"/><rect x="5" y="11" width="6" height="6"/><path d="M12 12h5v5h-5z" opacity=".7"/></svg></div>
    <span class="value-label">Integrity</span>
  </div>
  <div class="value" style="top:462px">
    <div class="value-icon"><svg width="20" height="20" viewBox="0 0 20 20" fill="#fff"><circle cx="7" cy="3" r="2"/><path d="M5 6h4l-1 6H6z"/><rect x="10" y="13" width="2" height="6"/><rect x="13" y="10" width="2" height="9"/><rect x="16" y="7" width="2" height="12"/><rect x="3" y="15" width="2" height="4"/></svg></div>
    <span class="value-label">Professional<br>Development</span>
  </div>

  <h2 class="abs leader-title">Our Leadership Team</h2>
  <div class="abs leader">
    <div class="leader-card">
      <div class="headshot" role="img" aria-label="Portrait photo of the president and CEO"></div>
      <div class="leader-name">Dana Whitfield</div>
      <div class="leader-role">MHA, MBA, CHCIO<br>President &amp; CEO</div>
    </div>
    Dana is the founder and CEO of BrevaLink Pro. Dana has been working in the technology industry for over 25 years with extensive experience in healthcare IT. Dana has held multiple roles including Chief Information Officer, Chief Information Security Officer, and the executive sponsor of multiple electronic health record (EHR) implementations. Dana has created and nurtured numerous successful IT departments and built strong relationships with leadership teams. Dana holds a Master's in Business Administration and a Master's in Healthcare Administration, and is certified with the Health Technology Leadership Council (HTLC).
  </div>
  <div class="abs contact">
    <div class="contact-line"><svg width="8" height="8" viewBox="0 0 10 10" fill="#4f2d8c"><path d="M2 0l2 2.5-1.2 1.3a6 6 0 0 0 3.4 3.4L7.5 6 10 8 8.5 10C4 10 0 6 0 1.5z"/></svg>555-014-2290</div>
    <div class="contact-line"><svg width="9" height="7" viewBox="0 0 10 8" fill="#4f2d8c"><rect width="10" height="8" rx="1"/><path d="M0 1l5 3.5L10 1" stroke="#fff" stroke-width=".9" fill="none"/></svg>dwhitfield@brevalinkpro.com</div>
    <div class="contact-line"><svg width="9" height="9" viewBox="0 0 10 10"><circle cx="5" cy="5" r="5" fill="#4f2d8c"/><path d="M3 2c1 1 2 1 2 2.5S3 6 3.5 8M6.5 5.5c1 .5 1.5 1.5 1 2.5" stroke="#fff" stroke-width=".8" fill="none"/></svg>www.brevalinkpro.com</div>
  </div>
  <div class="photo" role="img" aria-label="Team members giving a high five in an office" style="left:214px;top:346px;width:214px;height:164px;background:linear-gradient(135deg,#3a4350,#8a8f98 40%,#cfcfd2 60%,#2a2e36)"></div>

  <div class="block-purple" style="left:515px;top:214px;width:141px;height:140px"></div>
  <div class="photo" role="img" aria-label="Businessman pointing at a chart on a wall beside laptops" style="left:448px;top:45px;width:182px;height:316px;background:linear-gradient(160deg,#6a6d72,#3a3c40 45%,#1a1b1e)"></div>
  <div class="abs cover-text cover-1">Increasing</div>
  <div class="abs cover-text cover-2">The Value &amp;</div>
  <div class="abs cover-text cover-3">Security of Your</div>
  <div class="abs cover-text cover-4">Technology Resources</div>

  <div class="abs brand"><span class="brand-square"></span>BrevaLink Pro</div>
  <div class="abs web"><svg width="13" height="13" viewBox="0 0 10 10"><circle cx="5" cy="5" r="5" fill="#1d1d1d"/><path d="M3 2c1 1 2 1 2 2.5S3 6 3.5 8M6.5 5.5c1 .5 1.5 1.5 1 2.5" stroke="#fff" stroke-width=".8" fill="none"/></svg>www.brevalinkpro.com</div>
  <div class="abs rule"></div>
  <div class="abs rule-dot"></div>
  <div class="photo" role="img" aria-label="Technology tree illustration with connected icons" style="left:590px;top:448px;width:64px;height:62px;background:radial-gradient(circle at 50% 35%,#5fb7e6,#3b5fbf 55%,rgba(255,255,255,0) 72%)"></div>
</section>

<section class="sheet sheet-inside" aria-label="Brochure inside spread">
  <div class="block-purple" style="left:0;top:0;width:179px;height:174px"></div>
  <div class="photo" role="img" aria-label="Overhead view of a meeting table with laptops, notebooks and coffee" style="left:28px;top:43px;width:207px;height:206px;background:linear-gradient(135deg,#5b5048,#b08e6a 40%,#c9a985 60%,#3a3632)"></div>

  <h2 class="abs objectives-title">Our Primary<br>Objectives</h2>
  <div class="objective" style="top:362px">
    <div class="objective-icon"><svg width="20" height="20" viewBox="0 0 20 20" fill="none" stroke="#fff" stroke-width="1.2"><circle cx="10" cy="6" r="4"/><path d="M6 6h8M10 2v8"/><circle cx="4" cy="14" r="1.6"/><circle cx="10" cy="14" r="1.6"/><circle cx="16" cy="14" r="1.6"/><path d="M1.5 19c.5-2 4.5-2 5 0M7.5 19c.5-2 4.5-2 5 0M13.5 19c.5-2 4.5-2 5 0"/></svg></div>
    <p class="objective-text">Understand and exceed client expectations</p>
  </div>
  <div class="objective" style="top:408px">
    <div class="objective-icon"><svg width="22" height="16" viewBox="0 0 22 16" fill="#fff"><path d="M0 4l4-2 4 3 3-2 4 1 3-2 4 2v5l-3 1-5 5-3-2-4 1-4-4-3-1z"/></svg></div>
    <p class="objective-text">Committed to be a partner, not vendor</p>
  </div>
  <div class="objective" style="top:454px">
    <div class="objective-icon"><svg width="22" height="22" viewBox="0 0 22 22" fill="none" stroke="#fff" stroke-width="1.1"><circle cx="11" cy="11" r="4"/><circle cx="11" cy="11" r="1.5" fill="#fff"/><circle cx="11" cy="2.5" r="1.5"/><circle cx="11" cy="19.5" r="1.5"/><circle cx="2.5" cy="11" r="1.5"/><circle cx="19.5" cy="11" r="1.5"/><path d="M11 4v3M11 15v3M4 11h3M15 11h3"/></svg></div>
    <p class="objective-text">Provide simplified change management expertise</p>
  </div>

  <div class="abs services" role="img" aria-label="Dark photo of hands working at a laptop keyboard"></div>
  <div class="abs services-box"></div>
  <div class="abs services-our">Our</div>
  <h2 class="abs services-title">Services</h2>
  <p class="abs services-copy">We understand different organizations have different needs. BrevaLink Pro strives to assist your organization by bringing solutions that are easy to understand and allow the client to track success. We provide solutions based on the client's needs and desires.</p>
  <h3 class="abs services-head" style="font-weight:400">Information Technology</h3>
  <ul class="abs services-list">
    <li><svg width="8" height="7" viewBox="0 0 8 7"><path d="M1 4l2 2 4-5" stroke="#7b5cc4" stroke-width="1.3" fill="none"/></svg>CIO or IT Director Services</li>
    <li><svg width="8" height="7" viewBox="0 0 8 7"><path d="M1 4l2 2 4-5" stroke="#7b5cc4" stroke-width="1.3" fill="none"/></svg>CISO or Information Security Officer</li>
    <li><svg width="8" height="7" viewBox="0 0 8 7"><path d="M1 4l2 2 4-5" stroke="#7b5cc4" stroke-width="1.3" fill="none"/></svg>Comprehensive ePHI Risk Assessments</li>
    <li><svg width="8" height="7" viewBox="0 0 8 7"><path d="M1 4l2 2 4-5" stroke="#7b5cc4" stroke-width="1.3" fill="none"/></svg>IT Department Evaluation</li>
    <li><svg width="8" height="7" viewBox="0 0 8 7"><path d="M1 4l2 2 4-5" stroke="#7b5cc4" stroke-width="1.3" fill="none"/></svg>Policy Management and Consulting</li>
    <li><svg width="8" height="7" viewBox="0 0 8 7"><path d="M1 4l2 2 4-5" stroke="#7b5cc4" stroke-width="1.3" fill="none"/></svg>On-going IT department support</li>
  </ul>

  <h2 class="abs about-title">About Us</h2>
  <h3 class="abs about-head" style="top:70px;font-weight:400">Our Mission</h3>
  <p class="abs about-copy" style="top:86px">Partner with clients to increase the value and security of their technology tools.</p>
  <h3 class="abs about-head" style="top:117px;font-weight:400">Our Goal</h3>
  <p class="abs about-copy" style="top:135px">Become the premiere consulting company for Information Technology in the long term care industry.</p>
  <h3 class="abs about-head" style="top:185px;font-weight:400">Our Leaders</h3>
  <p class="abs about-copy" style="top:201px">Dana Whitfield, MHA, MBA, CHCIO</p>

  <div class="block-purple" style="left:550px;top:309px;width:136px;height:223px"></div>
  <div class="photo" role="img" aria-label="Finger touching hexagon icons labelled IT, data and computer" style="left:458px;top:251px;width:184px;height:191px;background:linear-gradient(135deg,#9fb4cc,#3f6fae 45%,#1d4f97 65%,#6c8fbd)"></div>
  <div class="photo" role="img" aria-label="Technology tree illustration with connected icons" style="left:460px;top:454px;width:82px;height:78px;background:radial-gradient(circle at 50% 35%,#5fb7e6,#3b5fbf 55%,rgba(255,255,255,0) 72%)"></div>
</section>

</body>
</html>
```